AN ELEGANT COSMETIC LABLE THAT CAN EASILY BE ALTERED TO FIT A VARIETY OF DIFFERENT PRODUCTS.

Predictable and ordinary designs are NOT welcome. Creative minds wanted.

Looking for a professional lable that is Canadian/USA Standard and compliant with the Food and Drug - Cosmetic Act in Onatrio. Which has a clean and elegant look, with a hint of holistic vibes.

This lable should be sleak and flexible to be altered to fit a variety of different products. Let your creativity come out with this project, the crazy and unpredictable are welcome.

This lable may be on the next biggest Cosmetic brand in the world. If you can see it, you can design it. All the best, looking forward to working with you.

Target Market(s)

Everyone who is looking for a clean natural lifestyle. The elite crowd.

Industry/Entity Type

Cosmetics

Font styles to use
Serif
Script

Colors

Designer to choose only greyscale colors for use in the design.

Requirements
Must have
• Company Name " BRELLOW'S" and or Logo. See attachment
Nice to have
• One or more solid bars that can be colored to match the main product ingredient colour.
Should not have
• Too much different colors or images

```html
<!DOCTYPE html>
<html lang="en">
<head>
<meta charset="utf-8">
<title>BRELLOW'S Aloe Vera Skin Soother Label</title>
<link rel="stylesheet" href="https://fonts.googleapis.com/css2?family=Playfair+Display:wght@700;800&family=Yeseva+One&family=Crimson+Pro:wght@700&family=Kaushan+Script&display=swap">
<style>
  :root {
    --bg-deep: #0b0d0b;
    --bg-mid: #1a1d1a;
    --leaf-bright: #7ddc3a;
    --leaf-mid: #3f9a1c;
    --leaf-dark: #14350c;
    --badge-green: #5fb043;
    --ink: #ffffff;
    --panel-dark: #0e120e;
  }
  * { margin: 0; padding: 0; box-sizing: border-box; }
  html, body { width: 1200px; height: 557px; overflow: hidden; background: var(--bg-deep); }
  .label {
    position: relative; width: 1200px; height: 557px; overflow: hidden;
    background: radial-gradient(ellipse at 50% 60%, var(--bg-mid), var(--bg-deep) 75%);
    color: var(--ink);
    font-family: "Crimson Pro", Georgia, serif;
  }
  .heading { position: absolute; font-family: "Yeseva One", Georgia, serif; font-size: 20px; line-height: 24px; font-weight: 400; }
  .copy { position: absolute; font-weight: 700; white-space: nowrap; }
  .copy--left { left: 39px; font-size: 15.5px; line-height: 18.5px; }
  .copy--right { left: 834px; font-size: 13.4px; line-height: 15.6px; }

  .centre-panel {
    position: absolute; left: 393px; top: 0; width: 414px; height: 557px;
    background: linear-gradient(160deg, var(--leaf-bright) 0%, var(--leaf-mid) 18%, var(--leaf-dark) 55%, var(--panel-dark) 100%);
  }
  .centre-frame {
    position: absolute; left: 24px; top: 39px; width: 348px; height: 489px;
    background: linear-gradient(180deg, #060806, #0d150c 70%, #132511);
  }
  .brand {
    position: absolute; left: 393px; width: 414px; top: 44px; text-align: center;
    font-family: "Playfair Display", Georgia, serif; font-weight: 800; font-size: 52px; line-height: 70px; letter-spacing: 1px; color: var(--ink);
  }
  .plant-art {
    position: absolute; left: 400px; top: 112px; width: 400px; height: 270px;
    background: radial-gradient(ellipse at 50% 75%, #6cc83e 0%, #3d8f22 40%, rgba(20,53,12,0.2) 75%, transparent 80%);
  }
  .variant { position: absolute; left: 393px; width: 414px; top: 380px; line-height: 30px; text-align: center; font-family: "Playfair Display", Georgia, serif; font-size: 25px; font-weight: 700; color: #f3ffe8; text-shadow: 0 0 8px var(--leaf-bright); }
  .product-name { position: absolute; left: 393px; width: 414px; text-align: center; font-family: "Kaushan Script", cursive; color: var(--ink); white-space: nowrap; }
  .product-name--en { top: 410px; font-size: 56px; line-height: 66px; }
  .product-name--fr { top: 472px; font-size: 44px; line-height: 54px; }
  .net-weight { position: absolute; left: 393px; width: 414px; top: 528px; line-height: 20px; text-align: center; font-family: "Playfair Display", Georgia, serif; font-size: 16px; font-weight: 700; letter-spacing: 3px; }

  .badge { position: absolute; width: 74px; text-align: center; color: var(--badge-green); }
  .badge svg { display: block; margin: 0 auto; }
  .badge span { display: block; font-weight: 700; font-size: 16px; line-height: 17px; margin-top: 4px; }
</style>
</head>
<body>
<main class="label">

  <h2 class="heading" style="left:39px;top:33px;">Ingredients:</h2>
  <p class="copy copy--left" style="top:64px;">Aloe gel, coconut oil, water, cetearyl alcohol,<br>glycerin, sunflower oil, shea butter, glycerin<br>stearate, beeswax, dimethicon, phenoxyethanol,<br>sodium polyacrylate, vitamin E.</p>

  <h2 class="heading" style="left:39px;top:173px;">Ingrédients :</h2>
  <p class="copy copy--left" style="top:205px;">Gel d'aloès, huile de noix de coco, eau, alcool<br>cetearyl, glycérine, huile de tournesol, beurre de<br>karité, stéarate de glycérine, cire d'abeille,<br>diméthicone, phénoxyethanol, polyacrylate de<br>sodium, vitamine E.</p>

  <h2 class="heading" style="left:39px;top:329px;">Warning:</h2>
  <p class="copy copy--left" style="top:360px;">This product is not intended for human<br>consumption. If irritation occurs, discontinue use.</p>

  <h2 class="heading" style="left:39px;top:432px;">Attention:</h2>
  <p class="copy copy--left" style="top:462px;">Ce produit n'est pas destiné à la<br>consommation humaine. En cas<br>d'irritation, cesser l'utilisation</p>

  <section class="centre-panel"><div class="centre-frame"></div></section>
  <div class="brand">BRELLOW'S</div>
  <div class="plant-art" role="img" aria-label="Photograph of a fresh aloe vera plant with water droplets"></div>
  <div class="variant">ALOE VERA</div>
  <div class="product-name product-name--en">Skin Soother</div>
  <div class="product-name product-name--fr">Deep Soother</div>
  <div class="net-weight">453.59 g/16 oz</div>

  <h2 class="heading" style="left:834px;top:32px;">Details:</h2>
  <p class="copy copy--right" style="top:58px;">Luxuriously rich moisturizer that melts effortlessly<br>into the skin, leaving it soft and luminous. This new<br>and improved formulation is pH-optimized for glowing<br>skin that remains hydrated and protected all day long.<br>It leaves no sticky residues and is easy to spread while<br>still maintaining the look and feel of a premium product.</p>

  <div class="badge" style="left:831px;top:170px;"><svg width="57" height="57" viewBox="0 0 57 57"><circle cx="28.5" cy="28.5" r="26.5" fill="none" stroke="currentColor" stroke-width="2.5"/><circle cx="29" cy="32" r="10" fill="none" stroke="currentColor" stroke-width="2"/><path d="M10 47 L47 10" stroke="currentColor" stroke-width="2.5"/></svg><span>Fragrance<br>FREE</span></div>
  <div class="badge" style="left:904px;top:170px;"><svg width="57" height="57" viewBox="0 0 57 57"><circle cx="28.5" cy="28.5" r="26.5" fill="none" stroke="currentColor" stroke-width="2.5"/><path d="M28.5 14 V44 M28.5 22 l-6 -4 M28.5 22 l6 -4 M28.5 30 l-7 -4 M28.5 30 l7 -4" stroke="currentColor" stroke-width="2" fill="none"/><path d="M10 47 L47 10" stroke="currentColor" stroke-width="2.5"/></svg><span>Gluten<br>FREE</span></div>
  <div class="badge" style="left:978px;top:170px;"><svg width="57" height="57" viewBox="0 0 57 57"><circle cx="28.5" cy="28.5" r="26.5" fill="none" stroke="currentColor" stroke-width="2.5"/><path d="M28.5 13 C22 23 19 28 19 33 a9.5 9.5 0 0 0 19 0 C38 28 35 23 28.5 13 Z" fill="none" stroke="currentColor" stroke-width="2"/><path d="M10 47 L47 10" stroke="currentColor" stroke-width="2.5"/></svg><span>Phthalate<br>FREE</span></div>
  <div class="badge" style="left:1050px;top:170px;"><svg width="57" height="57" viewBox="0 0 57 57"><circle cx="28.5" cy="28.5" r="26.5" fill="none" stroke="currentColor" stroke-width="2.5"/><ellipse cx="29" cy="35" rx="11" ry="8" fill="none" stroke="currentColor" stroke-width="2"/><ellipse cx="23" cy="20" rx="3.5" ry="8" fill="none" stroke="currentColor" stroke-width="2"/><ellipse cx="33" cy="20" rx="3.5" ry="8" fill="none" stroke="currentColor" stroke-width="2"/><path d="M10 47 L47 10" stroke="currentColor" stroke-width="2.5"/></svg><span>Cruelty<br>FREE</span></div>

  <h2 class="heading" style="left:834px;top:277px;">Détails:</h2>
  <p class="copy copy--right" style="top:300px;">Hydratant riche et luxueux qui fond sans effort dans la<br>peau, la laissant douce et lumineuse. Cette nouvelle<br>formulation améliorée a un pH optimisé pour une peau<br>éclatante qui reste hydratée et protégée toute la journée.<br>Il ne laisse aucun résidu collant et est facile à étaler tout<br>en conservant l'apparence et la sensation d'un produit<br>haut de gamme.</p>

  <div class="badge" style="left:833px;top:423px;"><svg width="60" height="60" viewBox="0 0 57 57"><circle cx="28.5" cy="28.5" r="26.5" fill="none" stroke="currentColor" stroke-width="2.5"/><circle cx="29" cy="32" r="10" fill="none" stroke="currentColor" stroke-width="2"/><path d="M10 47 L47 10" stroke="currentColor" stroke-width="2.5"/></svg><span>Sans<br>parfum</span></div>
  <div class="badge" style="left:909px;top:423px;"><svg width="60" height="60" viewBox="0 0 57 57"><circle cx="28.5" cy="28.5" r="26.5" fill="none" stroke="currentColor" stroke-width="2.5"/><path d="M28.5 14 V44 M28.5 22 l-6 -4 M28.5 22 l6 -4 M28.5 30 l-7 -4 M28.5 30 l7 -4" stroke="currentColor" stroke-width="2" fill="none"/><path d="M10 47 L47 10" stroke="currentColor" stroke-width="2.5"/></svg><span>Sans<br>gluten</span></div>
  <div class="badge" style="left:984px;top:423px;"><svg width="60" height="60" viewBox="0 0 57 57"><circle cx="28.5" cy="28.5" r="26.5" fill="none" stroke="currentColor" stroke-width="2.5"/><path d="M28.5 13 C22 23 19 28 19 33 a9.5 9.5 0 0 0 19 0 C38 28 35 23 28.5 13 Z" fill="none" stroke="currentColor" stroke-width="2"/><path d="M10 47 L47 10" stroke="currentColor" stroke-width="2.5"/></svg><span>Sans<br>phtalate</span></div>
  <div class="badge" style="left:1060px;top:423px;"><svg width="60" height="60" viewBox="0 0 57 57"><circle cx="28.5" cy="28.5" r="26.5" fill="none" stroke="currentColor" stroke-width="2.5"/><ellipse cx="29" cy="35" rx="11" ry="8" fill="none" stroke="currentColor" stroke-width="2"/><ellipse cx="23" cy="20" rx="3.5" ry="8" fill="none" stroke="currentColor" stroke-width="2"/><ellipse cx="33" cy="20" rx="3.5" ry="8" fill="none" stroke="currentColor" stroke-width="2"/><path d="M10 47 L47 10" stroke="currentColor" stroke-width="2.5"/></svg><span>Cruelty<br>FREE</span></div>

</main>
</body>
</html>
```